I would love for my business card to be fun and sophisicated. The clients are people that could afford nice well crafted wigs. These wigs are not like granny wigs. The're for women who are stylish and what to look there best especially if they are dealing with cancer are some from of hair loss. Do not want the card to appear crowded with to much information. If I need to eliminate some data, let me know.
Thanks

Industry/Entity Type

Hair

Contact Information for Business Card

L Radiant Tresses, Marjorie Ellison, owner, stylist

Wigs/Studio Showroom
Extensions
Hair Replacement
Private Room

24683 Mesa Vista Loop, Suite. R
Irvine, CA 90871
(949) 555-0178
Email: tresses@lradianttresses-example.com
www.lradianttresses-example.com

```html
<!DOCTYPE html>
<html lang="en">
<head>
<meta charset="utf-8">
<title>L Radiant Tresses – Business Card</title>
<link rel="stylesheet" href="https://fonts.googleapis.com/css2?family=Saira:wght@400;500;600&display=swap">
<style>
  :root {
    --backdrop: #2b2c2e;
    --card: #ffffff;
    --indigo: #3d3a96;
    --divider: #6d6d70;
    --ink: #1e1e22;
  }
  * { margin: 0; padding: 0; box-sizing: border-box; }
  html, body { width: 1200px; height: 817px; overflow: hidden; }
  body {
    background: var(--backdrop);
    font-family: "Saira", "Arial", sans-serif;
    display: flex; align-items: center; justify-content: center;
  }
  .card {
    position: relative;
    width: 1000px; height: 572px;
    background: var(--card);
    border-radius: 40px;
    overflow: hidden;
  }
  .band { position: absolute; background: var(--indigo); }
  .band--top { left: 580px; right: 0; top: 150px; height: 40px; }
  .band--name { left: 0; width: 420px; top: 212px; height: 52px; }
  .band--accent { left: 680px; right: 0; top: 432px; height: 24px; }
  .band--address { left: 0; right: 0; top: 488px; height: 48px; }

  .brand {
    position: absolute; left: 48px; top: 112px;
    font-size: 46px; font-weight: 500; color: var(--indigo);
    letter-spacing: 1px; line-height: 1.2;
  }
  .person {
    position: absolute; left: 36px; top: 212px; height: 52px;
    display: flex; align-items: center; gap: 16px;
  }
  .person__name {
    color: #fff; font-size: 26px; font-weight: 500; letter-spacing: 1px;
    text-transform: uppercase;
  }
  .person__role {
    position: absolute; left: 436px; top: 212px; height: 52px;
    color: var(--indigo); font-size: 19px; font-weight: 500;
    text-transform: uppercase; letter-spacing: 1px;
    display: flex; align-items: center; gap: 14px;
  }
  .person__role::before {
    content: ""; width: 3px; height: 28px; background: var(--indigo);
  }

  .contact {
    position: absolute; top: 296px;
    display: flex; flex-direction: column; align-items: center; gap: 18px;
  }
  .contact--phone { left: 0; width: 270px; }
  .contact--email { left: 270px; width: 410px; }
  .contact--web { left: 680px; width: 320px; }
  .contact__icon {
    width: 68px; height: 68px; border-radius: 50%;
    background: var(--indigo);
    display: flex; align-items: center; justify-content: center;
  }
  .contact__text {
    font-size: 18px; color: var(--ink); letter-spacing: 0.5px;
    white-space: nowrap;
  }
  .contact--phone .contact__text { font-size: 22px; letter-spacing: 1px; }

  .divider { position: absolute; width: 3px; background: var(--divider); top: 300px; height: 108px; }
  .divider--one { left: 270px; }
  .divider--two { left: 680px; }

  .address {
    position: absolute; left: 40px; top: 488px; height: 48px;
    display: flex; align-items: center; gap: 16px;
    color: #fff; font-size: 19px; letter-spacing: 1.5px;
  }
</style>
</head>
<body>
  <article class="card">
    <div class="band band--top"></div>
    <div class="band band--name"></div>
    <div class="band band--accent"></div>
    <div class="band band--address"></div>

    <h1 class="brand">L Radiant Tresses</h1>

    <div class="person">
      <svg width="32" height="38" viewBox="0 0 34 40" aria-hidden="true">
        <circle cx="17" cy="11" r="9" fill="#fff"/>
        <path d="M2 40 C2 27 9 22 17 22 C25 22 32 27 32 40 Z" fill="#fff"/>
      </svg>
      <span class="person__name">Marjorie Ellison</span>
    </div>
    <div class="person__role">Owner, Stylist</div>

    <div class="contact contact--phone">
      <div class="contact__icon">
        <svg width="26" height="40" viewBox="0 0 28 42" aria-hidden="true">
          <rect x="1.5" y="1.5" width="25" height="39" rx="4" fill="none" stroke="#fff" stroke-width="3"/>
          <rect x="5" y="7" width="18" height="25" fill="#fff"/>
          <circle cx="14" cy="36" r="2" fill="#fff"/>
        </svg>
      </div>
      <span class="contact__text">(949) 555-0178</span>
    </div>

    <div class="divider divider--one"></div>

    <div class="contact contact--email">
      <div class="contact__icon">
        <svg width="36" height="25" viewBox="0 0 38 26" aria-hidden="true">
          <rect x="1" y="1" width="36" height="24" fill="#fff"/>
          <path d="M1 1 L19 15 L37 1" fill="none" stroke="#3d3a96" stroke-width="2.5"/>
        </svg>
      </div>
      <span class="contact__text">tresses@lradianttresses-example.com</span>
    </div>

    <div class="divider divider--two"></div>

    <div class="contact contact--web">
      <div class="contact__icon">
        <svg width="38" height="38" viewBox="0 0 40 40" aria-hidden="true" fill="none" stroke="#fff" stroke-width="2.5">
          <circle cx="20" cy="20" r="17"/>
          <ellipse cx="20" cy="20" rx="8" ry="17"/>
          <line x1="3" y1="20" x2="37" y2="20"/>
          <line x1="20" y1="3" x2="20" y2="37"/>
          <path d="M6 11 H34 M6 29 H34"/>
        </svg>
      </div>
      <span class="contact__text">www.lradianttresses-example.com</span>
    </div>

    <div class="address">
      <svg width="20" height="28" viewBox="0 0 22 30" aria-hidden="true">
        <path d="M11 0 C4.9 0 0 4.9 0 11 C0 19 11 30 11 30 C11 30 22 19 22 11 C22 4.9 17.1 0 11 0 Z" fill="#fff"/>
        <circle cx="11" cy="11" r="4" fill="#3d3a96"/>
      </svg>
      <span>24683 Mesa Vista Loop, Suite. R, Irvine, CA 90871</span>
    </div>
  </article>
</body>
</html>
```